spot uv business card design for KLT Mechanics

I need a great new business card design best suited for spot uv printing. Details to include are Oliver Haskett 0491227304 wwwkltmech.com.au, oli@kltmech.com.au. Company logo attached.
The design has to be spot uv/varnish optimised!!

```html
<!DOCTYPE html>
<html lang="en">
<head>
<meta charset="utf-8">
<title>KLT Mechanics – Business Card Concepts</title>
<link href="https://fonts.googleapis.com/css2?family=Barlow:wght@300;400;500&display=swap" rel="stylesheet">
<style>
  :root {
    --navy: #3b5677;
    --navy-deep: #334d6c;
    --navy-faint: #304866;
    --paper: #ffffff;
    --frame: #4a4a4a;
    --ink-light: #ffffff;
  }
  * { box-sizing: border-box; margin: 0; padding: 0; }
  html, body {
    width: 1077px; height: 1200px; overflow: hidden; background: var(--paper);
    font-family: "Barlow", Arial, sans-serif;
  }
  .sheet {
    position: relative; width: 1077px; height: 1200px;
    border: 2px solid var(--frame);
  }
  .card {
    position: absolute; width: 448px; height: 249px; overflow: hidden;
  }
  .card--front {
    left: 59px;
    border-radius: 8px 54px 8px 54px;
    background: var(--paper);
    border: 1.5px solid #2b2b2b;
    display: flex; align-items: center; justify-content: center;
  }
  .card--front.card--dark { background: var(--navy); border-color: var(--navy); }
  .card--back {
    left: 571px;
    border-radius: 54px 8px 54px 8px;
    background: var(--navy);
    color: var(--ink-light);
  }
  .row-1 { top: 33px; }
  .row-2 { top: 324px; }
  .row-3 { top: 618px; }
  .row-4 { top: 898px; }

  .brand {
    display: flex; align-items: center; gap: 12px;
    font-weight: 300; font-size: 37px; letter-spacing: 0.5px;
    color: var(--navy);
  }
  .brand__mark { width: 26px; height: 26px; background: var(--navy); }
  .card--dark .brand { color: var(--navy-faint); }
  .card--dark .brand__mark { background: var(--navy-faint); }

  .back-texture { position: absolute; inset: 0; background: var(--navy); }

  .details { position: absolute; inset: 0; }
  .name { font-size: 21px; font-weight: 400; }
  .line { font-size: 16px; font-weight: 400; }
  .small { font-size: 15px; font-weight: 400; }

  .details--centered .name { position: absolute; top: 47px; width: 100%; text-align: center; }
  .details--centered .phone { position: absolute; top: 75px; width: 100%; text-align: center; }
  .details--centered .footer { position: absolute; top: 210px; right: 66px; white-space: nowrap; }

  .details--stacked .name { position: absolute; left: 46px; top: 102px; }
  .details--stacked .phone { position: absolute; left: 46px; top: 155px; }
  .details--stacked .email { position: absolute; left: 46px; top: 186px; }
  .details--stacked .web { position: absolute; left: 46px; top: 208px; }

  .details--icons .name { position: absolute; left: 37px; top: 102px; }
  .contact { position: absolute; left: 35px; display: flex; align-items: center; gap: 8px; }
  .contact svg { width: 15px; height: 15px; flex: none; }
  .contact--phone { top: 161px; }
  .contact--email { top: 189px; }
  .contact--web { top: 211px; }
</style>
</head>
<body>
<div class="sheet">

  <!-- Concept 1 -->
  <div class="card card--front row-1">
    <div class="brand"><span class="brand__mark"></span>KLT MECHANICS</div>
  </div>
  <div class="card card--back row-1">
    <div class="back-texture" role="img" aria-label="Spot UV pattern of repeated company names on navy"></div>
    <div class="details details--centered">
      <p class="name">Oliver Haskett</p>
      <p class="line phone">0491 227 304</p>
      <p class="small footer">oli@kltmech.com.au | wwwkltmech.com.au</p>
    </div>
  </div>

  <!-- Concept 2 -->
  <div class="card card--front card--dark row-2">
    <div class="brand"><span class="brand__mark"></span>KLT MECHANICS</div>
  </div>
  <div class="card card--back row-2">
    <div class="back-texture" role="img" aria-label="Spot UV pattern of repeated company names on navy"></div>
    <div class="details details--centered">
      <p class="name">Oliver Haskett</p>
      <p class="line phone">0491 227 304</p>
      <p class="small footer">oli@kltmech.com.au | wwwkltmech.com.au</p>
    </div>
  </div>

  <!-- Concept 3 -->
  <div class="card card--front row-3">
    <div class="brand"><span class="brand__mark"></span>KLT MECHANICS</div>
  </div>
  <div class="card card--back row-3">
    <div class="back-texture" role="img" aria-label="Spot UV pattern of repeated company names on navy"></div>
    <div class="details details--stacked">
      <p class="name">Oliver Haskett</p>
      <p class="line phone">0491 227 304</p>
      <p class="small email">oli@kltmech.com.au</p>
      <p class="small web">wwwkltmech.com.au</p>
    </div>
  </div>

  <!-- Concept 4 -->
  <div class="card card--front row-4">
    <div class="brand"><span class="brand__mark"></span>KLT MECHANICS</div>
  </div>
  <div class="card card--back row-4">
    <div class="back-texture" role="img" aria-label="Spot UV pattern of repeated company names on navy"></div>
    <div class="details details--icons">
      <p class="name">Oliver Haskett</p>
      <div class="contact contact--phone">
        <svg viewBox="0 0 16 16" aria-hidden="true"><path fill="#fff" d="M3.6 1.5l2.2 2.6-1.3 1.6c.9 2 2.3 3.5 4.3 4.4l1.6-1.3 2.6 2.2-1.4 2.1C6.9 13.4 2.6 9.1 1.5 4.4z"/></svg>
        <span class="line">0491 227 304</span>
      </div>
      <div class="contact contact--email">
        <svg viewBox="0 0 16 16" aria-hidden="true"><rect x="1.5" y="4" width="13" height="9" fill="#fff"/><path d="M1.5 4l6.5 5 6.5-5" fill="none" stroke="#3b5677" stroke-width="1.3"/></svg>
        <span class="small">oli@kltmech.com.au</span>
      </div>
      <div class="contact contact--web">
        <svg viewBox="0 0 16 16" aria-hidden="true"><circle cx="8" cy="8" r="6.5" fill="#fff"/><path d="M1.5 8h13M8 1.5c-2.5 3-2.5 10 0 13M8 1.5c2.5 3 2.5 10 0 13" fill="none" stroke="#3b5677" stroke-width="1"/></svg>
        <span class="small">wwwkltmech.com.au</span>
      </div>
    </div>
  </div>

</div>
</body>
</html>
```